nine-parts.com

We are a small dollar lending company that will revolutionize the industry. We will do this by being completely transparent, fee free, etc and an interest rate that normal people can afford to pay. Over 10X less than our competition. We only allow our members to pay bills " bills paid fast", within 72 hours. Payday loans typically charge from 390%-600% with a terrible payback structure. We charge 36%, period, with a payback structure over 12 months. Our site will be very simple and easy to use but elegant at the same time. We do not want the site to be too busy, less is more and easier. We will have; Home, The Story, Why 9parts.com, Are you eligible? Members, Clients. To become a member you have to be referred by a current client of 9parts.com. A lot of the busy stuff will be saved for the Members and Clients sections. The feel must be elegant, easy to use and very simple to understand. I am looking for the green, white and black combinations of colors, very similar to my logo that was designed by Pixelmoor.

```html
<!DOCTYPE html>
<html lang="en">
<head>
<meta charset="utf-8">
<title>nine-parts.com – Bills Paid Fast</title>
<link rel="stylesheet" href="https://fonts.googleapis.com/css2?family=Lora:ital,wght@0,400;0,700;1,400;1,700&family=Open+Sans:wght@400;600;700&display=swap">
<style>
  :root{
    --green:#7cc242;
    --green-dark:#5fa52c;
    --green-soft:#a6d77c;
    --ink:#222222;
    --text:#6b6b6b;
    --muted:#9a9a9a;
    --line:#e3e3e3;
    --white:#ffffff;
    --footer:#2b2b2b;
    --footer-text:#bdbdbd;
  }
  *{box-sizing:border-box;margin:0;padding:0}
  html,body{width:769px;height:1200px;overflow:hidden;background:var(--white)}
  body{font-family:"Open Sans",Arial,sans-serif;color:var(--text);font-size:9px;line-height:1.5;position:relative}
  a{color:inherit;text-decoration:none}

  /* Header */
  .site-header{position:absolute;top:0;left:0;width:769px;height:74px;display:flex;align-items:center;justify-content:space-between;padding:0 28px 0 26px}
  .brand{display:flex;align-items:center;gap:6px;font-weight:700;font-size:19px;color:var(--ink);letter-spacing:.5px}
  .brand-dot{width:22px;height:22px;border-radius:50%;background:var(--green)}
  .main-nav{display:flex;align-items:center;gap:16px;font-size:10px;color:var(--ink)}
  .main-nav .active{color:var(--green);border-bottom:1px solid var(--green);padding-bottom:2px}
  .login-btn{background:var(--green);color:var(--white);padding:4px 14px;font-weight:600}

  /* Hero */
  .hero{position:absolute;top:74px;left:0;width:769px;height:386px;overflow:hidden}
  .hero-photo{position:absolute;inset:0;background:linear-gradient(100deg,#d9dcd8 0%,#c9ced0 30%,#b6b8b2 55%,#e6e2dc 80%,#f3f1ee 100%)}
  .hero-caption{position:absolute;left:0;top:210px;width:560px;height:92px;background:linear-gradient(90deg,rgba(0,0,0,.45),rgba(0,0,0,0));padding:12px 0 0 36px}
  .hero-title{font-family:"Lora",Georgia,serif;font-style:italic;font-weight:700;font-size:34px;color:var(--white);line-height:1.1}
  .hero-sub{font-family:"Lora",Georgia,serif;font-style:italic;font-size:12.5px;color:var(--white);margin-top:8px}
  .hero-arrow{position:absolute;top:160px}
  .hero-arrow.prev{left:10px}
  .hero-arrow.next{right:10px}

  /* Feature band */
  .features{position:absolute;top:460px;left:0;width:769px;height:106px;background:linear-gradient(180deg,var(--white) 0 14px,var(--green) 14px 100%)}
  .feature-row{position:absolute;top:22px;left:34px;right:34px;display:flex;gap:10px}
  .feature{flex:1;height:64px;background:var(--green-soft);border:1px solid rgba(255,255,255,.6);display:flex;align-items:flex-start;gap:8px;padding:10px 12px}
  .feature-icon{width:34px;height:34px;flex:none;border-radius:3px;background:linear-gradient(135deg,#e9b56a,#b77b35)}
  .feature h3{font-family:"Lora",Georgia,serif;font-style:italic;font-size:9px;color:var(--ink);font-weight:700;margin-bottom:2px}
  .feature p{font-size:7px;line-height:1.45;color:#3d5a26}

  /* Welcome */
  .welcome{position:absolute;top:594px;left:0;width:769px;text-align:center}
  .welcome-title{display:inline-flex;align-items:center;gap:6px;font-size:15px;font-weight:700;color:var(--ink);letter-spacing:.6px}
  .welcome-title .brand-dot{width:18px;height:18px}
  .welcome p{width:520px;margin:12px auto 0;font-size:7.5px;color:var(--muted);line-height:1.6}
  .cta{display:inline-block;margin-top:14px;background:var(--green);color:var(--white);font-family:"Lora",Georgia,serif;font-style:italic;font-weight:700;font-size:9.5px;padding:6px 18px}

  /* Columns */
  .content-row{position:absolute;top:766px;left:34px;width:701px;display:flex;gap:18px}
  .column{width:182px}
  .column h2{font-family:"Lora",Georgia,serif;font-size:12px;color:var(--ink);font-weight:700;margin-bottom:8px}
  .column-photo{height:90px;margin-bottom:8px}
  .column-photo.story{background:linear-gradient(135deg,#d8d2c8,#7a6e60)}
  .column-photo.members{background:linear-gradient(135deg,#f0f0ee,#c2c4c6)}
  .column p{font-size:7px;color:var(--muted);line-height:1.55}
  .column .more{color:var(--green);font-weight:600}
  .newsletter{margin-left:auto;width:201px;height:200px;background:var(--green);padding:12px 12px}
  .newsletter h2{font-family:"Lora",Georgia,serif;font-style:italic;font-size:10px;color:var(--white);font-weight:700;border-bottom:1px solid rgba(255,255,255,.35);padding-bottom:6px}
  .newsletter p{font-size:7px;color:var(--white);margin:8px 0 10px;line-height:1.5}
  .field{height:18px;background:var(--green-soft);border:1px solid rgba(255,255,255,.5);color:var(--white);font-size:7px;padding:3px 6px;margin-bottom:8px}
  .submit{display:inline-block;background:var(--green-dark);color:var(--white);font-size:7.5px;padding:4px 14px}
  .slider-dots{position:absolute;top:984px;right:34px;display:flex;gap:4px}

  /* Clients */
  .clients{position:absolute;top:1010px;left:34px;width:701px;border-top:1px solid var(--line);display:flex;justify-content:space-around;align-items:center;height:50px}
  .client{font-size:11px;font-weight:600;color:#b5b5b5}

  /* Footer */
  .site-footer{position:absolute;top:1086px;left:0;width:769px;height:114px;background:var(--footer);text-align:center;padding-top:18px}
  .social{display:flex;justify-content:center;gap:8px}
  .social span{width:16px;height:16px;border-radius:50%;background:#555}
  .footer-nav{margin-top:16px;display:flex;justify-content:center;gap:14px;font-size:7.5px;color:var(--footer-text)}
  .copyright{margin-top:10px;font-size:6.5px;color:#8a8a8a}
</style>
</head>
<body>

<header class="site-header">
  <a class="brand" href="#"><span class="brand-dot"></span>NINE PARTS</a>
  <nav class="main-nav">
    <a class="active" href="#">Home</a>
    <a href="#">The Story</a>
    <a href="#">Why 9parts.com</a>
    <a href="#">Are you eligible? Members</a>
    <a href="#">Clients</a>
    <a class="login-btn" href="#">Login</a>
  </nav>
</header>

<section class="hero">
  <div class="hero-photo" role="img" aria-label="Smiling young woman at a laptop in a bright home setting"></div>
  <div class="hero-caption">
    <h1 class="hero-title">Bills Paid Fast</h1>
    <p class="hero-sub">Charge only 36% and give over 12 months time to pay back, no fees, hidden costs</p>
  </div>
  <svg class="hero-arrow prev" width="14" height="34" viewBox="0 0 14 34"><polyline points="12,2 2,17 12,32" fill="none" stroke="#8f8f8f" stroke-width="3"/></svg>
  <svg class="hero-arrow next" width="14" height="34" viewBox="0 0 14 34"><polyline points="2,2 12,17 2,32" fill="none" stroke="#8f8f8f" stroke-width="3"/></svg>
</section>

<section class="features">
  <div class="feature-row">
    <div class="feature">
      <div class="feature-icon" role="img" aria-label="Small illustration of a wallet"></div>
      <div><h3>Lorem ipsum dummy text</h3><p>Lorem ipsum is simply dummy text of the printing and typesetting industry ipsum dolor.</p></div>
    </div>
    <div class="feature">
      <div class="feature-icon" role="img" aria-label="Small illustration of a document"></div>
      <div><h3>Lorem ipsum dummy text</h3><p>Lorem ipsum is simply dummy text of the printing and typesetting industry ipsum dolor.</p></div>
    </div>
    <div class="feature">
      <div class="feature-icon" role="img" aria-label="Small illustration of a money bag"></div>
      <div><h3>Lorem ipsum dummy text</h3><p>Lorem ipsum is simply dummy text of the printing and typesetting industry ipsum dolor.</p></div>
    </div>
  </div>
</section>

<section class="welcome">
  <h2 class="welcome-title">WELCOME TO <span class="brand-dot"></span>NINE PARTS</h2>
  <p>Lorem ipsum dolor sit amet, consectetur adipiscing elit, sed do eiusmod tempor incididunt ut labore et dolore magna aliqua. Ut enim ad minim veniam, quis nostrud exercitation ullamco laboris nisi ut aliquip ex ea commodo consequat. Duis aute irure dolor in reprehenderit in voluptate velit esse cillum dolore eu fugiat nulla pariatur. Excepteur sint occaecat cupidatat non proident, sunt in culpa qui officia deserunt mollit anim.</p>
  <a class="cta" href="#">Click Here For More Info</a>
</section>

<section class="content-row">
  <article class="column">
    <h2>The Story</h2>
    <div class="column-photo story" role="img" aria-label="Hands typing on a laptop keyboard"></div>
    <p>Lorem ipsum dolor sit amet, consectetur adipiscing elit. Sed do eiusmod tempor incididunt ut labore et dolore magna aliqua. <a class="more" href="#">Read More</a></p>
  </article>
  <article class="column">
    <h2>Members</h2>
    <div class="column-photo members" role="img" aria-label="Woman working at a desk with a computer"></div>
    <p>Lorem ipsum dolor sit amet, consectetur adipiscing elit. Sed do eiusmod tempor incididunt ut labore et dolore magna aliqua. <a class="more" href="#">Read More</a></p>
  </article>
  <aside class="newsletter">
    <h2>News Letter</h2>
    <p>Lorem ipsum dolor sit amet, consectetur adipiscing elit, sed do eiusmod tempor.</p>
    <div class="field">Enter Name</div>
    <div class="field">Email Id</div>
    <span class="submit">Submit</span>
  </aside>
</section>

<div class="slider-dots">
  <svg width="8" height="10" viewBox="0 0 8 10"><polyline points="6,1 2,5 6,9" fill="none" stroke="var(--green)" stroke-width="2"/></svg>
  <svg width="8" height="10" viewBox="0 0 8 10"><polyline points="2,1 6,5 2,9" fill="none" stroke="var(--green)" stroke-width="2"/></svg>
</div>

<section class="clients">
  <span class="client">Harbor Lane</span>
  <span class="client">Ideafold</span>
  <span class="client">Midora</span>
  <span class="client">Okera</span>
  <span class="client">Sunvale</span>
</section>

<footer class="site-footer">
  <div class="social"><span></span><span></span><span></span></div>
  <nav class="footer-nav">
    <a href="#">Home</a><span>|</span>
    <a href="#">The Story</a><span>|</span>
    <a href="#">Why 9parts.com</a><span>|</span>
    <a href="#">Are you eligible? Members</a><span>|</span>
    <a href="#">Clients</a>
  </nav>
  <p class="copyright">Copyright 2013 nine-parts.com All Rights Reserved</p>
</footer>

</body>
</html>
```